Edgy Fun BBQ sauce label Needed

We are looking for a new label design as we are going to start to sell our competition bbq sauce. We have had multiple 1st place wins using this sauce in NPGL BBQ competitions

The Sauce name is Drizzle Away! The sauce will be bottled in mason jars, I would like the label to play off bbq themes and "sweet heat"

The sauce will be bottled in standard mason jar 16 oz and the label size is (2.3125in” x 9.4375in ) the front logo needs to fit with in (2.3125 tall x 5in across) Since the back will have to have the food label info.

We are looking for a new label design as we are going to start to sell our competition bbq sauce. We have had multiple 1st place wins using this sauce in NPGL BBQ competitions so I would like to have award winning ribbon somewhere on the label.

We have a logo for our BBQ team this can be incorporated but it is not required. If it is incorporated to the design. it does not have to be the focal point.

We are looking for this label to stand out and grab their attention we like to have fun and push the envelope a bit so don't be timid with the design.

Sauce Description: The award winning Sizzle Up! BBQ team has been bringing our local flavor to the BBQ competition circuit and now we are bringing it straight to your kitchen. Slather Sweat heat on any meat.

Here are some examples of sauces that are popular in competition bbq.

http://hamcratesmokehouse.example/

https://www.tallgrillsupply.example/store/bbq-sauce/jade-goat-classic-barbecue-sauce

https://www.tallgrillsupply.example/store/bbq-sauce/fieldhands-tangy-240
Updates

I would like to see on the label  in a the sauce name "Drizzle Away!"  then in smaller front "Barbecue Sauce"  - Then optional in yet smaller front "A Sweet Heat Treat" or " A Sweet Heat Treat for any Meat"

With all this I understand the Sizzle Up logo may not fit which is ok and it does not need to be on the label.

Project Deadline Extended
Reason: I know a bunch of Designers had just started to work on this project so I extended the deadline..

Target Market(s)

We are going to focus on catering, farmers markets, fairs, and BBQ competitions

Industry/Entity Type

Store

Font styles to use
Other font styles liked:
• Desdemona

Colors
eb1f27
f37022
fcf9ce
fbed23
faa54b

Requirements
Must have
• The Sauce name - Drizzle Away!
smaller then name but I would like " BBQ Sauce - Treat your meat to a sweet heat"

award winning ribbon or trophy
Nice to have
• A edgy cartoon pig or cow standing over a kestor style kettle grill using a mop style brush slathering sauce on to a rack of bbq ribs

Sizzle Up! BBQ in matching front from our logo

```html
<!DOCTYPE html>
<html lang="en">
<head>
<meta charset="utf-8">
<title>Drizzle Away!! Barbecue Sauce Label</title>
<link rel="stylesheet" href="https://fonts.googleapis.com/css2?family=Bubblegum+Sans&family=Limelight&family=Roboto+Condensed:wght@400;700&display=swap">
<style>
  :root {
    --page: #ececec;
    --maroon: #6e0000;
    --black: #050505;
    --orange: #f37022;
    --orange-bright: #f7911e;
    --amber: #faa54b;
    --yellow: #fbed23;
    --cream: #fcf9ce;
    --red: #eb1f27;
    --deep-red: #7a0c0c;
    --side-text: #f5c518;
    --gold: #d6a531;
    --navy: #1c2d6b;
  }
  * { margin: 0; padding: 0; box-sizing: border-box; }
  html, body { width: 1200px; height: 1000px; overflow: hidden; background: var(--page); }
  .canvas { position: relative; width: 1200px; height: 1000px; }

  .label {
    position: absolute; left: 46px; top: 367px;
    width: 1094px; height: 266px;
    display: flex;
    box-shadow: 0 2px 6px rgba(0,0,0,.15);
  }
  .panel-side { background: var(--maroon); width: 256px; position: relative; }
  .panel-front { background: var(--black); width: 581px; position: relative; overflow: hidden; }
  .panel-back { width: 257px; }

  .team-mark {
    position: absolute; left: 92px; top: 14px;
    width: 64px; height: 76px;
    display: flex; flex-direction: column; align-items: center; justify-content: center; gap: 6px;
    font-family: "Roboto Condensed", sans-serif; font-weight: 700; font-size: 11px;
    color: var(--side-text); text-align: center; line-height: 1.1;
  }
  .team-mark-square { width: 22px; height: 22px; background: var(--amber); }

  .story {
    position: absolute; left: 34px; top: 98px; width: 210px;
    font-family: "Roboto Condensed", sans-serif; font-size: 10.5px; line-height: 1.25;
    color: var(--side-text);
  }

  .facts {
    position: absolute; left: 94px; top: 64px;
    list-style: none;
    font-family: "Roboto Condensed", sans-serif; font-size: 10.5px;
    color: var(--side-text);
  }
  .facts li { margin-bottom: 14px; }

  .splash {
    position: absolute; left: 0; top: -10px; width: 360px; height: 190px;
    border-radius: 48% 52% 45% 55% / 50% 45% 55% 50%;
    background: radial-gradient(ellipse at 55% 50%, var(--amber) 0%, var(--orange) 45%, #d9401a 80%, rgba(180,30,10,0) 100%);
  }

  .front-band {
    position: absolute; left: 0; bottom: 0; width: 100%; height: 89px;
    background: var(--orange-bright);
  }

  .sauce-name {
    position: absolute; left: 140px; top: 40px; width: 360px;
    text-align: center;
    font-family: "Bubblegum Sans", cursive; font-size: 74px; line-height: 0.86;
    text-transform: uppercase;
    color: var(--yellow);
    background: linear-gradient(180deg, var(--yellow) 0%, var(--amber) 45%, var(--orange) 100%);
    -webkit-background-clip: text; background-clip: text;
    -webkit-text-fill-color: transparent;
    -webkit-text-stroke: 2px var(--deep-red);
    filter: drop-shadow(2px 3px 0 var(--deep-red));
  }

  .award-ribbon { position: absolute; left: 86px; top: 142px; width: 54px; height: 100px; }

  .product-type {
    position: absolute; left: 168px; top: 186px;
    font-family: "Limelight", serif; font-size: 33px; line-height: 1;
    color: var(--cream);
    -webkit-text-stroke: 1.5px var(--deep-red);
    text-shadow: 2px 2px 0 var(--deep-red);
    text-transform: uppercase; letter-spacing: 0.5px;
  }
  .tagline {
    position: absolute; left: 262px; top: 230px;
    font-family: "Limelight", serif; font-size: 21px; line-height: 1;
    color: var(--deep-red); text-transform: uppercase;
  }
</style>
</head>
<body>
<main class="canvas">
  <section class="label" aria-label="Drizzle Away barbecue sauce wrap label">
    <div class="panel-side panel-story">
      <div class="team-mark">
        <span class="team-mark-square"></span>
        <span>Sizzle Up!</span>
      </div>
      <p class="story">The award winning Sizzle Up! BBQ team has been bringing our local flavor to the BBQ competition circuit and now we are bringing it straight to your kitchen. Slather Sweat heat on any meat.</p>
    </div>

    <div class="panel-front">
      <div class="splash" role="img" aria-label="Glossy orange sauce splash with small farm animal outlines"></div>
      <div class="front-band"></div>
      <h1 class="sauce-name">Drizzle<br>Away!!</h1>
      <svg class="award-ribbon" viewBox="0 0 54 100" aria-label="First place award ribbon">
        <polygon points="12,46 4,96 18,86 27,98 27,50" fill="var(--navy)"/>
        <polygon points="42,46 50,96 36,86 27,98 27,50" fill="var(--navy)"/>
        <circle cx="27" cy="30" r="27" fill="var(--gold)"/>
        <circle cx="27" cy="30" r="21" fill="var(--navy)"/>
        <circle cx="27" cy="30" r="16" fill="var(--cream)"/>
      </svg>
      <p class="product-type">Barbecue Sauce</p>
      <p class="tagline">A Sweet Heat Treat</p>
    </div>

    <div class="panel-side panel-back">
      <ul class="facts">
        <li>Ingredients:</li>
        <li>Nutrition Facts:</li>
        <li>Food distributor info</li>
      </ul>
    </div>
  </section>
</main>
</body>
</html>
```